Redesign business cards

We have a new logo and I am not that happy with the layout of our existing card and looking for a change. Font is a bit small and the green can be hard to read. Logo may need a tidy up as the copy I have is not that hi-res too so require you to produce a hi-res version of the logo for us too. There will be three individual business cards to produce with just the names and phone numbers being different. Address will change too, but use what you see on the card for now.

Industry/Entity Type

Business

Requirements
Nice to have
• You could consider a redesign to the new logo, just not too radical. We like the blue and green hexagons as we feel that they are representative of oil industry that we are in.

```html
<!DOCTYPE html>
<html lang="en">
<head>
<meta charset="utf-8">
<title>Verdane Oil Services – Business Cards</title>
<link href="https://fonts.googleapis.com/css2?family=Marcellus+SC&display=swap" rel="stylesheet">
<style>
  :root {
    --bg: #e9e7e3;
    --card: #ffffff;
    --green: #8cc63f;
    --green-deep: #6fa82a;
    --grey: #6d6e71;
    --ink: #4a4b4d;
    --white: #ffffff;
  }
  * { margin: 0; padding: 0; box-sizing: border-box; }
  html, body {
    width: 1200px; height: 900px; overflow: hidden;
    background: var(--bg);
    font-family: "Marcellus SC", "Times New Roman", serif;
  }
  .canvas { position: relative; width: 1200px; height: 900px; }

  .card {
    position: absolute;
    background: var(--card);
    border-radius: 40px;
    overflow: hidden;
    box-shadow: 0 6px 18px rgba(0,0,0,0.12);
  }
  .card-front { left: 60px; top: 50px; width: 760px; height: 440px; }
  .card-back { left: 420px; top: 525px; width: 600px; height: 347px; }

  .card-art { position: absolute; inset: 0; width: 100%; height: 100%; }

  .brand { position: absolute; display: flex; align-items: center; color: var(--ink); }
  .brand-mark { background: var(--green); flex: none; }
  .brand-text { display: flex; flex-direction: column; line-height: 1; }
  .brand-name { letter-spacing: 1px; }
  .brand-sub { letter-spacing: 1px; }

  .card-front .brand { right: 70px; top: 70px; gap: 16px; }
  .card-front .brand-mark { width: 46px; height: 46px; }
  .card-front .brand-name { font-size: 58px; }
  .card-front .brand-sub { font-size: 22px; margin-top: 6px; }

  .card-back .brand { left: 50%; top: 50%; transform: translate(-50%, -50%); gap: 14px; }
  .card-back .brand-mark { width: 40px; height: 40px; }
  .card-back .brand-name { font-size: 50px; }
  .card-back .brand-sub { font-size: 19px; margin-top: 5px; }

  .person { position: absolute; left: 500px; top: 226px; line-height: 1.1; }
  .person-name { color: var(--green-deep); font-size: 30px; letter-spacing: 1px; }
  .person-role { color: var(--ink); font-size: 26px; margin-top: 4px; letter-spacing: 1px; }

  .contact {
    position: absolute; left: 30px; top: 218px;
    list-style: none; color: var(--white);
    font-size: 17px; line-height: 22px; letter-spacing: 0.4px;
  }
  .contact li { display: flex; align-items: flex-start; gap: 8px; }
  .contact-icon { width: 15px; height: 15px; margin-top: 3px; flex: none; }
</style>
</head>
<body>
<main class="canvas">

  <section class="card card-front" aria-label="Business card front">
    <svg class="card-art" viewBox="0 0 760 440" aria-hidden="true">
      <path d="M0,75 C120,40 210,100 270,225 C330,345 430,385 760,385 L760,440 L0,440 Z" fill="#8cc63f"/>
      <path d="M30,32 C160,20 260,80 320,200 C380,310 470,345 760,345 L760,368 C460,372 360,330 300,215 C245,100 160,45 30,32 Z" fill="#6d6e71"/>
    </svg>

    <div class="brand">
      <span class="brand-mark"></span>
      <div class="brand-text">
        <span class="brand-name">Verdane</span>
        <span class="brand-sub">Oil Services</span>
      </div>
    </div>

    <div class="person">
      <p class="person-name">Daniel Hart</p>
      <p class="person-role">Owner / C.E.O</p>
    </div>

    <ul class="contact">
      <li>
        <svg class="contact-icon" viewBox="0 0 14 14"><circle cx="7" cy="7" r="7" fill="#fff"/><path d="M7,3 L11,6.5 L10,6.5 L10,10.5 L4,10.5 L4,6.5 L3,6.5 Z" fill="#8cc63f"/></svg>
        <span>Suite # 410, Elm Bldg,<br>NY 10458</span>
      </li>
      <li>
        <svg class="contact-icon" viewBox="0 0 14 14"><circle cx="7" cy="7" r="7" fill="#fff"/><path d="M4.5,3.5 L6,3.5 L6.8,5.6 L5.8,6.4 C6.3,7.5 6.9,8.1 8,8.6 L8.8,7.6 L10.8,8.4 L10.8,9.9 C8,10.4 4.2,6.8 4.5,3.5 Z" fill="#8cc63f"/></svg>
        <span>555-201-3344</span>
      </li>
      <li>
        <svg class="contact-icon" viewBox="0 0 14 14"><circle cx="7" cy="7" r="7" fill="#fff"/><rect x="4.8" y="3" width="4.4" height="8" rx="1" fill="#8cc63f"/></svg>
        <span>555-872-1190</span>
      </li>
      <li>
        <svg class="contact-icon" viewBox="0 0 14 14"><circle cx="7" cy="7" r="7" fill="#fff"/><rect x="3.5" y="5.5" width="7" height="4.5" fill="#8cc63f"/><rect x="5" y="3.5" width="4" height="2" fill="#8cc63f"/></svg>
        <span>555-430-6578</span>
      </li>
      <li>
        <svg class="contact-icon" viewBox="0 0 14 14"><circle cx="7" cy="7" r="7" fill="#fff"/><rect x="3.5" y="4.5" width="7" height="5" fill="#8cc63f"/><path d="M3.5,4.5 L7,7.5 L10.5,4.5" fill="none" stroke="#fff" stroke-width="0.8"/></svg>
        <span>daniel@verdaneoil.com</span>
      </li>
      <li>
        <svg class="contact-icon" viewBox="0 0 14 14"><circle cx="7" cy="7" r="7" fill="#fff"/><circle cx="7" cy="7" r="3.6" fill="none" stroke="#8cc63f" stroke-width="1.1"/><path d="M3.4,7 L10.6,7 M7,3.4 L7,10.6" stroke="#8cc63f" stroke-width="0.9"/></svg>
        <span>www.verdaneoil.com</span>
      </li>
    </ul>
  </section>

  <section class="card card-back" aria-label="Business card back">
    <div class="brand">
      <span class="brand-mark"></span>
      <div class="brand-text">
        <span class="brand-name">Verdane</span>
        <span class="brand-sub">Oil Services</span>
      </div>
    </div>
  </section>

</main>
</body>
</html>
```